Fresh looking flyer for Vellmar Institute Of Computing

We need a flyer design for our IT school that will be distributed to potential students during our recruitment campaign. We want to feature the following aspects of the school:

-Study IT in a nordic/european way close to your home (design should feel Scandinavian)
-Featuring the dean of the school (photo attached)
-Match the theme of logo (logo attached)
-A potential layout attached as a mockup

CONTENT
* Main Message " LEARN EUROPEAN PROGRAMMING COURSES IN BEKASI"
* Sub Message " 3 MONTH MODULES FROM BEGINNER TO ADVANCED"
* Campaign " ATTEND FREE CLASS & GET 10% OFF COURSE, SIGN UP BETWEEN 7-18MARCH. vellmar.example/free
* Extra info: " GRADUATE AND GET HIRED TO EARN 120 MILLION IDR/YEAR"

End result should be in Adobe Illustrator format.

Target Market(s)

18-30 year old Indonesians interested in IT

Industry/Entity Type

Education

Font styles to use
Sans Serif

Colors
85cae6

Requirements
Must have
• -Photo of the manager
• -Messages as in the project description
• -School logo
• -Nordic look and feel

```html
<!DOCTYPE html>
<html lang="en">
<head>
<meta charset="utf-8">
<title>Vellmar Institute Of Computing – Flyer</title>
<link rel="stylesheet" href="https://fonts.googleapis.com/css2?family=Barlow:wght@700&family=Lato:wght@400;700&display=swap">
<style>
  :root {
    --stage: #3a3a3c;
    --sky: #85cae6;
    --sky-pale: #b3e0ee;
    --ice: #a9c7e6;
    --navy: #123f6e;
    --royal: #3f5fb0;
    --teal: #29bcd2;
    --steel: #8c98a6;
    --ink: #2f2f31;
    --white: #ffffff;
  }
  * { margin: 0; padding: 0; box-sizing: border-box; }
  html, body {
    width: 1200px; height: 881px; overflow: hidden;
    background: var(--stage);
  }
  .flyer {
    position: absolute; left: 59px; top: 58px;
    width: 1083px; height: 765px; overflow: hidden;
    background: var(--sky);
  }
  .flyer-backdrop { position: absolute; inset: 0; }
  .headline {
    position: absolute; left: 54px; top: 76px;
    font-family: "Barlow", sans-serif; font-weight: 700;
    font-size: 61px; line-height: 60px; color: var(--navy);
    letter-spacing: 0.2px;
  }
  .sub-message {
    position: absolute; left: 54px; top: 275px;
    font-family: "Barlow", sans-serif; font-weight: 700;
    font-size: 39px; line-height: 41px; color: var(--ink);
  }
  .campaign {
    position: absolute; left: 54px; top: 376px;
    font-family: "Lato", sans-serif; font-weight: 700; color: var(--navy);
  }
  .campaign-line { font-size: 25px; line-height: 30px; }
  .campaign-offer { font-size: 39px; line-height: 44px; }
  .campaign-url { font-size: 35px; line-height: 48px; margin-top: 2px; }
  .brand {
    position: absolute; left: 54px; top: 660px;
    display: flex; align-items: center; gap: 18px;
    font-family: "Lato", sans-serif; font-weight: 400;
    font-size: 24px; line-height: 31px; color: var(--white);
  }
  .brand-mark {
    width: 44px; height: 44px; border-radius: 50%;
    background: var(--white); flex: none;
  }
  .salary-badge {
    position: absolute; left: 675px; top: 641px;
    width: 408px; height: 101px;
    background: var(--navy); border-radius: 50px 0 0 50px;
    padding: 19px 21px 0 0; text-align: right;
    font-family: "Lato", sans-serif; font-weight: 700;
    font-size: 22px; line-height: 31px; color: var(--white);
  }
</style>
</head>
<body>
<main class="flyer">
  <svg class="flyer-backdrop" width="1083" height="765" viewBox="0 0 1083 765" aria-hidden="false">
    <defs>
      <linearGradient id="sky-wash" x1="0" y1="0" x2="0.4" y2="1">
        <stop offset="0" stop-color="#7fcbdc"/>
        <stop offset="0.5" stop-color="#a6dcec"/>
        <stop offset="1" stop-color="#9cb8e2"/>
      </linearGradient>
      <linearGradient id="portrait-tone" x1="0" y1="0" x2="0" y2="1">
        <stop offset="0" stop-color="#d9b98f"/>
        <stop offset="0.35" stop-color="#e9c3ab"/>
        <stop offset="0.6" stop-color="#f1f1f1"/>
        <stop offset="1" stop-color="#ffffff"/>
      </linearGradient>
    </defs>
    <rect class="sky-field" width="1083" height="765" fill="url(#sky-wash)"/>
    <polygon points="110,0 740,0 560,300" fill="#ffffff" opacity="0.18"/>
    <polygon points="0,90 560,300 600,470 0,420" fill="#ffffff" opacity="0.1"/>
    <!-- angled stripes -->
    <polygon points="745,0 1083,0 1083,110 700,110" fill="var(--royal)"/>
    <polygon points="880,0 1083,0 1083,95 860,60" fill="var(--teal)"/>
    <polygon points="745,0 800,0 650,220 620,220" fill="#3d4c7e"/>
    <polygon points="680,105 1083,105 1083,145 660,145" fill="#a7adb6"/>
    <polygon points="650,145 1083,145 1083,180 630,180" fill="#5e6670"/>
    <polygon points="690,180 1083,180 1083,490 820,490" fill="#ffffff"/>
    <polygon points="730,165 760,165 585,500 560,500" fill="var(--steel)"/>
    <polygon points="760,180 800,180 610,560 575,560" fill="#c1c7cf"/>
    <polygon points="500,495 1083,480 1083,530 490,545" fill="#4b5aa8"/>
    <polygon points="1000,470 1083,460 1083,500 990,505" fill="#4a7f86"/>
    <polygon points="520,540 1083,525 1083,560 510,575" fill="var(--royal)"/>
    <!-- bottom band -->
    <path d="M0,590 C180,600 350,625 480,645 L540,640 L540,765 L0,765 Z" fill="var(--navy)"/>
    <polygon points="470,650 560,560 640,560 560,680" fill="#3e55a2"/>
    <!-- portrait area -->
    <path role="img" aria-label="Portrait photo of the school's dean, smiling, glasses, white shirt"
      d="M730,60 C790,40 880,45 920,90 C940,130 930,220 920,270 C940,300 930,340 905,345
         C895,390 880,420 860,440 L880,470 C960,500 1030,520 1083,540 L1083,765 L437,765
         C460,680 500,600 600,560 C640,545 690,520 700,460 C680,430 660,380 655,330
         C625,320 625,280 645,270 C640,200 665,100 730,60 Z" fill="url(#portrait-tone)"/>
  </svg>

  <h1 class="headline">LEARN EUROPEAN<br>PROGRAMMING<br>COURSES IN BEKASI</h1>

  <p class="sub-message">3 MONTH MODULES FROM<br>BEGINNER TO ADVANCED</p>

  <div class="campaign">
    <p class="campaign-line">ATTEND FREE CLASS &amp; GET</p>
    <p class="campaign-offer">10% OFF COURSE,</p>
    <p class="campaign-line">SIGN UP BETWEEN 7-18 MARCH</p>
    <p class="campaign-url">vellmar.example/free</p>
  </div>

  <div class="brand">
    <span class="brand-mark"></span>
    <span class="brand-name">VELLMAR INSTITUTE<br>OF COMPUTING</span>
  </div>

  <p class="salary-badge">GRADUATE AND GET HIRED TO<br>EARN 120 MILLION IDR/YEAR</p>
</main>
</body>
</html>
```